Essential Oil 15ml - package of 6

Design of a box of 6 different essential oils.
+ design of the bottle stickers
My bottles are 15ml clear blue glass.

The pictures attached are my competitors...

Target Market(s)

BRAMBLEWICK USA

Font styles to use
Serif

Requirements
Must have
• Our logo + "essential oil" and type (lavender, eucalyptus etc....)
• 15ml - 0.50 fl.oz.
• special color for the oil type.

```html
<!DOCTYPE html>
<html lang="en">
<head>
<meta charset="utf-8">
<title>Dunewell Essential Oil Labels</title>
<link rel="stylesheet" href="https://fonts.googleapis.com/css2?family=Cinzel:wght@400;600&family=Cormorant+Garamond:wght@500;600&display=swap">
<style>
  :root {
    --canvas: #000000;
    --ink: #2a2622;
    --band: rgba(30, 30, 34, 0.82);
    --tangerine-light: #f7c23a;
    --tangerine-mid: #eda51f;
    --tangerine-deep: #d98a12;
    --tangerine-type: #c9951f;
    --lavender-light: #e04ff0;
    --lavender-mid: #b73ad6;
    --lavender-deep: #7e2aa4;
    --lavender-type: #8a34b0;
  }
  * { margin: 0; padding: 0; box-sizing: border-box; }
  html, body { width: 1200px; height: 1200px; overflow: hidden; background: var(--canvas); }
  .canvas { position: relative; width: 1200px; height: 1200px; }
  .label {
    position: absolute;
    top: 404px;
    width: 340px;
    height: 430px;
    overflow: hidden;
    text-align: center;
    color: var(--ink);
  }
  .label--tangerine { left: 97px; }
  .label--lavender { left: 763px; }
  .label__backdrop { position: absolute; inset: 0; }
  .label--tangerine .label__backdrop {
    background: radial-gradient(ellipse at 55% 30%, var(--tangerine-light), var(--tangerine-mid) 55%, var(--tangerine-deep));
  }
  .label--lavender .label__backdrop {
    background: radial-gradient(ellipse at 50% 30%, var(--lavender-light), var(--lavender-mid) 60%, var(--lavender-deep));
  }
  .label__content { position: relative; }
  .brand { margin-top: 44px; }
  .brand__mark {
    display: block;
    width: 92px; height: 92px;
    margin: 0 auto 18px;
    border-radius: 50%;
    background: var(--ink);
  }
  .brand__name {
    font-family: "Cinzel", serif;
    font-weight: 600;
    font-size: 46px;
    line-height: 1;
    color: var(--ink);
  }
  .label__kind {
    margin-top: 24px;
    font-family: "Cormorant Garamond", serif;
    font-weight: 600;
    font-size: 21px;
    letter-spacing: 1px;
  }
  .label__band {
    margin-top: 8px;
    height: 50px;
    background: var(--band);
    font-family: "Cinzel", serif;
    font-weight: 400;
    font-size: 43px;
    line-height: 52px;
    letter-spacing: 2px;
  }
  .label--tangerine .label__band { color: var(--tangerine-type); }
  .label--lavender .label__band { color: var(--lavender-type); }
  .label__grade {
    margin-top: 8px;
    font-family: "Cormorant Garamond", serif;
    font-weight: 500;
    font-size: 17px;
  }
  .label__volume {
    margin-top: 66px;
    font-family: "Cormorant Garamond", serif;
    font-weight: 500;
    font-size: 17px;
  }
</style>
</head>
<body>
<main class="canvas">
  <section class="label label--tangerine">
    <div class="label__backdrop" role="img" aria-label="Soft close-up photograph of tangerine segments in golden orange tones"></div>
    <div class="label__content">
      <div class="brand">
        <span class="brand__mark"></span>
        <div class="brand__name">Dunewell</div>
      </div>
      <p class="label__kind">100% ESSENTIAL OIL</p>
      <p class="label__band">TANGERINE</p>
      <p class="label__grade">PURE THERAPEUTIC GRADE</p>
      <p class="label__volume">15ml - 0.50 fl.oz.</p>
    </div>
  </section>

  <section class="label label--lavender">
    <div class="label__backdrop" role="img" aria-label="Soft photograph of lavender sprigs in violet and magenta tones"></div>
    <div class="label__content">
      <div class="brand">
        <span class="brand__mark"></span>
        <div class="brand__name">Dunewell</div>
      </div>
      <p class="label__kind">100% ESSENTIAL OIL</p>
      <p class="label__band">LAVENDER</p>
      <p class="label__grade">PURE THERAPEUTIC GRADE</p>
      <p class="label__volume">15ml - 0.50 fl.oz.</p>
    </div>
  </section>
</main>
</body>
</html>
```